SOLENTIVA extra virgin olive oil label

We need a label design for a new range of products dedicated to the kitchen professionals. Ideally the label will be rectangular with a H10cm L15cm
The label needs to include the following:
Solentiva Logo
Olio Extravergine d'Oliva
1lt
Nutritional panel (see attached file)
Best before
Lot code
Product of Italy
Superior Category olive oil obtained directly from olives by mechanical processes only
Imported in Australia by
Ingredients: extra virgin olive oil
Produced and bottled by:
The final design should communicate quality, value and consistency to the kitchen professionals
The VESKO pasta sauce label can be a good example of the style we are after. see attached file

Target Market(s)

Kitchen professionals
The catch phrase is:
Bringing quality value and consistency to the kitchen professionals

This catch parse SHOULD NOT be included in the label

Industry/Entity Type

Kitchen

Font styles to use
Serif

Requirements
Must have
• Easy to read and easy to remember

```html
<!DOCTYPE html>
<html lang="en">
<head>
<meta charset="utf-8">
<title>Solentiva Extra Virgin Olive Oil – Label</title>
<link rel="stylesheet" href="https://fonts.googleapis.com/css2?family=EB+Garamond:ital,wght@0,400;0,500;0,600;1,400&family=Arimo:wght@700&display=swap">
<style>
  :root {
    --page: #f2f0e6;
    --card: #ffffff;
    --card-edge: #d9d5c2;
    --ink: #111111;
    --brand-red: #e0262b;
    --volume-grey: #d4d4d4;
    --olive-dark: #6f7d2c;
    --olive-light: #b8c46a;
    --panel-line: #111111;
  }
  html, body {
    margin: 0;
    padding: 0;
    width: 785px;
    height: 1200px;
    overflow: hidden;
    background: var(--page);
  }
  .canvas {
    position: relative;
    width: 785px;
    height: 1200px;
    font-family: "EB Garamond", "Book Antiqua", serif;
    color: var(--ink);
  }
  .side-caption {
    position: absolute;
    top: 30px;
    font-family: "Arimo", Arial, sans-serif;
    font-weight: 700;
    font-size: 22px;
  }
  .side-caption--front { left: 18px; }
  .side-caption--back { left: 382px; }

  .label {
    position: absolute;
    top: 80px;
    width: 320px;
  }
  .label--front { left: 50px; }
  .label--back { left: 415px; }

  .card {
    position: absolute;
    left: 0;
    width: 320px;
    background: var(--card);
    border: 1px solid var(--card-edge);
    border-radius: 26px;
    box-sizing: border-box;
  }
  .brand-card {
    top: 0;
    height: 230px;
    display: flex;
    align-items: center;
    justify-content: center;
    gap: 12px;
  }
  .brand-dot {
    width: 26px;
    height: 26px;
    border-radius: 50%;
    background: var(--brand-red);
  }
  .brand-name {
    font-size: 34px;
    font-weight: 600;
    letter-spacing: 2px;
    color: var(--brand-red);
  }

  .info-card {
    top: 240px;
    height: 820px;
  }
  .line {
    position: absolute;
    left: 0;
    right: 0;
    margin: 0;
    text-align: center;
    white-space: nowrap;
    line-height: 1.2;
  }

  .product-title {
    left: auto;
    right: 14px;
    top: 28px;
    font-style: italic;
    font-size: 21px;
  }
  .olive-branch {
    position: absolute;
    left: 8px;
    top: 100px;
    width: 150px;
    height: 150px;
    border-radius: 50%;
    background: radial-gradient(circle at 50% 50%, var(--olive-light), var(--olive-dark) 68%, transparent 71%);
  }
  .process-claim {
    position: absolute;
    right: 16px;
    top: 78px;
    margin: 0;
    text-align: right;
    font-style: italic;
    font-size: 22px;
    line-height: 32px;
  }

  .volume {
    font-size: 100px;
    font-weight: 600;
    color: var(--volume-grey);
    line-height: 1;
  }
  .product-name {
    font-size: 27px;
    font-weight: 500;
  }
  .detail {
    font-size: 21px;
  }
  .importer {
    font-style: italic;
    font-size: 23px;
  }

  .label--front .volume { top: 340px; }
  .label--front .product-name { top: 448px; }
  .detail--best { top: 512px; }
  .detail--lot { top: 570px; }
  .detail--origin { top: 627px; }
  .detail--producer { top: 685px; }
  .label--front .importer { top: 738px; }

  .label--back .volume { top: 2px; }
  .label--back .product-name { top: 100px; line-height: 36px; }
  .nutrition-heading {
    top: 206px;
    color: var(--brand-red);
    font-size: 27px;
    font-weight: 500;
    line-height: 36px;
  }
  .nutrition-panel {
    position: absolute;
    left: 16px;
    top: 285px;
    width: 288px;
    height: 442px;
    border: 3px solid var(--panel-line);
    border-radius: 28px;
    box-sizing: border-box;
  }
  .label--back .importer { top: 748px; }
</style>
</head>
<body>
<div class="canvas">
  <div class="side-caption side-caption--front">Front</div>
  <div class="side-caption side-caption--back">Back</div>

  <section class="label label--front">
    <div class="card brand-card">
      <span class="brand-dot"></span>
      <span class="brand-name">SOLENTIVA</span>
    </div>
    <div class="card info-card">
      <p class="line product-title">Olio Extravergine d'Oliva</p>
      <div class="olive-branch" role="img" aria-label="Illustration of an olive branch with green olives"></div>
      <p class="process-claim">olive oil obtained<br>directly from<br>olives by<br>mechanical<br>processes<br>only</p>
      <p class="line volume">1lt</p>
      <p class="line product-name">Extra virgin olive oil</p>
      <p class="line detail detail--best">Best before</p>
      <p class="line detail detail--lot">Lot code</p>
      <p class="line detail detail--origin">Product of Italy</p>
      <p class="line detail detail--producer">Produced and bottled by:</p>
      <p class="line importer">Imported in Australia by</p>
    </div>
  </section>

  <section class="label label--back">
    <div class="card brand-card">
      <span class="brand-dot"></span>
      <span class="brand-name">SOLENTIVA</span>
    </div>
    <div class="card info-card">
      <p class="line volume">1lt</p>
      <p class="line product-name">Extra virgin olive oil<br>Product of Italy</p>
      <p class="line nutrition-heading">Nutritional<br>Information</p>
      <div class="nutrition-panel"></div>
      <p class="line importer">Imported in Australia by</p>
    </div>
  </section>
</div>
</body>
</html>
```